Mellow Meadow

Hello,
I require the following to be completed for my business.
My company font is Spicy Rice, and I'm enclosing a picture of a logo.
Please amend the enclosed brochure to make it look better.(fieldgrovepamphlet6)
Please amend the enclosed installation guide, so it says my company name, addresses logo, etc on it (installation instructions).
Please create a letter head and business cards
My name is Tomas Verhundic and my title is National Sales Manager, company address is on the site: mellowmeadow.ca, tomas@mellowmeadow.ca cell phone is 416-295-6148, I'm thinking we have just the logo on one side and "Premium Synthetic Turf" in spicy font. On the letter head, on the bottom i'm thinking of showing grass come up, see my website.
The MM_ Label pages is required to create product labels, please add a colourmark of my company logo in the designs. (I'll require 6 or 8 per page, and more product are coming, let's just iron down layout. (my sites product page has more products)
Target Market(s)
The target market will be home owners.
Industry/Entity Type
Cell Phone
Logo Text
Design Build Innovate
Look and feel
Each slider illustrates characteristics of the customer's brand and the style your logo design should communicate.

```html
<!DOCTYPE html>
<html lang="en">
<head>
<meta charset="utf-8">
<title>Mellow Meadow Letterhead</title>
<link href="https://fonts.googleapis.com/css2?family=Spicy+Rice&display=swap" rel="stylesheet">
<style>
  :root {
    --paper: #bbdd8d;
    --edge: #8d9a84;
    --ink-green: #1c6a2c;
    --footer-curve: #d3e44c;
    --grass-light: #c9e56a;
    --grass-deep: #3f9a34;
  }
  html, body {
    margin: 0;
    padding: 0;
    width: 849px;
    height: 1200px;
    overflow: hidden;
    background: #ffffff;
  }
  .letterhead {
    position: relative;
    width: 849px;
    height: 1200px;
    box-sizing: border-box;
    background: var(--paper);
    border: 1px solid var(--edge);
    overflow: hidden;
    font-family: "Spicy Rice", cursive;
    color: var(--ink-green);
  }
  .brand-name {
    position: absolute;
    left: 40px;
    top: 78px;
    margin: 0;
    font-family: "Spicy Rice", cursive;
    font-weight: 400;
    font-size: 44px;
    line-height: 1;
    color: var(--ink-green);
    letter-spacing: 1px;
  }
  .services {
    position: absolute;
    right: 56px;
    top: 72px;
    width: 260px;
    margin: 0;
    text-align: center;
    font-size: 20px;
    line-height: 36px;
  }
  .footer-curve {
    position: absolute;
    left: 0;
    bottom: 0;
    width: 520px;
    height: 130px;
  }
  .footer-grass {
    position: absolute;
    right: 0;
    bottom: 0;
    width: 470px;
    height: 128px;
    background: linear-gradient(to top, var(--grass-deep) 0%, var(--grass-light) 55%, rgba(187, 221, 141, 0) 100%);
  }
  .contact {
    position: absolute;
    left: 33px;
    top: 1106px;
    margin: 0;
    font-size: 18px;
    line-height: 34px;
  }
  .contact .phone {
    display: block;
    padding-left: 18px;
  }
</style>
</head>
<body>
  <div class="letterhead">
    <h1 class="brand-name">Mellow Meadow</h1>

    <p class="services">Lawn &amp; Landscaping,<br>Playgrounds,<br>Pet Turf</p>

    <svg class="footer-curve" viewBox="0 0 520 130" aria-hidden="true">
      <path d="M0 18 C 120 -6, 300 0, 420 60 C 460 82, 485 108, 500 130 L 0 130 Z" fill="var(--footer-curve)"/>
    </svg>

    <div class="footer-grass" role="img" aria-label="Blades of green grass rising along the bottom edge"></div>

    <p class="contact">
      <span class="web">mellowmeadow.ca, tomas@mellowmeadow.ca</span>
      <span class="phone">cell phone 416-295-6148</span>
    </p>
  </div>
</body>
</html>
```